Clever Burrow

Create effective banner ads for the website CleverBurrow.com. We are building a re-target ad for coffee shops and/or stay at home office workers, and we would like to order 3 separate designs with the banner sizes 300x250, 728x90, 320x50, 640x100, 300x50, and 160x600, and they all need to be under 40kb of data. We have provided 9 slogans you can use in the Banner Ad Slogans and Extra Details document. Feel free to create your own slogan, and use resources found on our website.

Industry/Entity Type

Building

```html
<!DOCTYPE html>
<html lang="en">
<head>
<meta charset="utf-8">
<title>Clever Burrow – Real Office and Co-Working</title>
<link rel="stylesheet" href="https://fonts.googleapis.com/css2?family=Dancing+Script:wght@700&family=Open+Sans:wght@600;700;800&display=swap">
<style>
  :root {
    --orange: #e8691c;
    --orange-light: #f0842a;
    --orange-deep: #de561b;
    --white: #ffffff;
    --brick: #c0705a;
    --brick-dark: #a65a45;
    --floor: #7d6152;
    --floor-dark: #5a463b;
    --button-edge: #5a3212;
  }
  html, body {
    margin: 0;
    padding: 0;
    overflow: hidden;
  }
  body {
    width: 1200px;
    height: 1001px;
    background: var(--white);
  }
  .banner {
    position: relative;
    width: 1200px;
    height: 1001px;
    overflow: hidden;
    font-family: "Open Sans", Arial, sans-serif;
    color: var(--white);
  }
  .workspace-photo {
    position: absolute;
    inset: 0;
    background:
      radial-gradient(ellipse 700px 520px at 1000px 250px, var(--brick) 0%, var(--brick-dark) 55%, rgba(166,90,69,0) 100%),
      linear-gradient(150deg, var(--floor) 0%, var(--floor) 45%, var(--floor-dark) 100%);
  }
  .speech-shape {
    position: absolute;
    left: 0;
    top: 0;
    width: 930px;
    height: 700px;
  }
  .headline {
    position: absolute;
    margin: 0;
    font-family: "Dancing Script", cursive;
    font-weight: 700;
    line-height: 1;
    white-space: nowrap;
    text-align: center;
  }
  .headline-question { left: 60px; top: 60px; width: 790px; font-size: 86px; }
  .headline-answer { left: 50px; top: 172px; width: 720px; font-size: 110px; }
  .headline-answer-end { left: 190px; top: 296px; width: 470px; font-size: 110px; }
  .brand-name {
    position: absolute;
    left: 88px;
    top: 448px;
    margin: 0;
    font-size: 36px;
    font-weight: 700;
    line-height: 1.2;
  }
  .cta-button {
    position: absolute;
    left: 42px;
    top: 636px;
    width: 426px;
    height: 104px;
    border-radius: 52px;
    border: 4px solid var(--button-edge);
    box-sizing: border-box;
    background: linear-gradient(180deg, var(--orange-light) 0%, var(--orange) 55%, var(--orange-deep) 100%);
    color: var(--white);
    font-size: 66px;
    font-weight: 800;
    line-height: 94px;
    text-align: center;
    text-decoration: none;
  }
  .offer {
    position: absolute;
    left: 90px;
    top: 796px;
    margin: 0;
    font-size: 40px;
    font-weight: 700;
    line-height: 1.38;
  }
  .brand-mark {
    position: absolute;
    left: 848px;
    top: 634px;
    width: 272px;
    height: 272px;
    border-radius: 50%;
    border: 6px solid var(--white);
    box-sizing: border-box;
    display: flex;
    align-items: center;
    justify-content: center;
    font-size: 34px;
    font-weight: 700;
    color: var(--white);
    text-align: center;
    line-height: 1.3;
  }
</style>
</head>
<body>
  <main class="banner">
    <div class="workspace-photo" role="img" aria-label="Photo of two people working at white desks with a monitor and laptops in a brick-walled co-working office with a framed poster and concrete floor"></div>

    <svg class="speech-shape" viewBox="0 0 930 700" aria-hidden="true">
      <defs>
        <linearGradient id="speech-fill" x1="0" y1="0" x2="1" y2="1">
          <stop offset="0" stop-color="var(--orange-light)"/>
          <stop offset="1" stop-color="var(--orange-deep)"/>
        </linearGradient>
      </defs>
      <polygon points="0,0 890,0 890,190 575,400 250,540 40,680 0,680" fill="url(#speech-fill)"/>
    </svg>

    <h1 class="headline headline-question">What’s Your Address ?</h1>
    <p class="headline headline-answer">Second Table On</p>
    <p class="headline headline-answer-end">The Left ?</p>

    <p class="brand-name">Clever Burrow</p>

    <a class="cta-button" href="#">Click here</a>

    <p class="offer">Real Office and<br>Co-Working</p>

    <div class="brand-mark">Clever<br>Burrow</div>
  </main>
</body>
</html>
```